Brimovex business card

Based on company logo and website given , to design a business card temple. Slogan "Your furry friends deserves the best"
Color style please refer to our website

```html
<!DOCTYPE html>
<html lang="en">
<head>
<meta charset="utf-8">
<title>Brimovex business card</title>
<link rel="stylesheet" href="https://fonts.googleapis.com/css2?family=Montserrat:wght@400&family=Source+Serif+4:wght@400;600&display=swap">
<style>
  :root {
    --forest: #0c2d2b;
    --forest-deep: #1b302c;
    --gold: #b5a42e;
    --sun: #f4e22f;
    --olive: #bfb035;
    --paper: #f6f5f2;
    --stage-light: #efebe4;
    --stage-tan: #d8c3a8;
    --ink: #23302c;
    --white: #ffffff;
  }
  * { box-sizing: border-box; margin: 0; padding: 0; }
  html, body { width: 1200px; height: 1200px; overflow: hidden; }
  body { position: relative; background: var(--paper); font-family: "Source Serif 4", Georgia, serif; }

  .board-left { position: absolute; left: 0; top: 0; width: 422px; height: 1200px; }
  .hero-photo {
    position: absolute; left: 0; top: 0; width: 422px; height: 640px;
    background: linear-gradient(180deg, #56593f 0%, #7a5a3a 35%, #8d5532 55%, #3e4a3c 80%, var(--forest-deep) 100%);
  }
  .brand-panel {
    position: absolute; left: 0; top: 640px; width: 422px; height: 140px;
    background: var(--forest-deep);
    display: flex; align-items: flex-start; justify-content: center;
  }
  .brand-panel .wordmark { color: var(--sun); font-size: 72px; font-weight: 400; line-height: 1; letter-spacing: -1px; margin-top: -6px; }
  .about-panel {
    position: absolute; left: 0; top: 780px; width: 420px; height: 420px;
    background: var(--olive); color: var(--white);
    font-family: "Montserrat", Arial, sans-serif; font-size: 16.5px; line-height: 23.6px;
    text-align: center; padding: 138px 50px 0;
  }

  .stage-top { position: absolute; left: 422px; top: 0; width: 778px; height: 477px; background: var(--paper); }
  .stage-bottom {
    position: absolute; left: 422px; top: 477px; width: 778px; height: 723px;
    background: linear-gradient(90deg, var(--stage-light) 0 311px, var(--stage-tan) 311px 100%);
  }

  .card {
    position: absolute; overflow: hidden; border-radius: 2.6em;
    box-shadow: 0 0.4em 1.2em rgba(0,0,0,0.12);
  }
  .card--small { font-size: 7.5px; width: 345px; height: 197px; }
  .card--large { font-size: 10px; width: 459px; height: 266px; }
  .card--front { background: var(--forest); color: var(--white); }
  .card--front.card--large { background: var(--forest-deep); }
  .card--back { background: var(--white); }

  .card__logo { position: absolute; text-align: center; }
  .card__logo .wordmark { display: block; color: var(--gold); line-height: 1; letter-spacing: -0.03em; }
  .card__logo .slogan { display: block; line-height: 1.3; }

  .card--front .card__logo { left: 0; right: 0; top: 40%; }
  .card--front .wordmark { font-size: 4.2em; }
  .card--front .slogan { color: var(--white); font-weight: 600; font-size: 1.1em; margin-top: 0.2em; }
  .card--front.card--large .slogan { font-size: 1.25em; }
  .card--front .site { position: absolute; left: 0; right: 0; top: 87%; text-align: center; font-size: 0.9em; letter-spacing: 0.05em; color: var(--white); }

  .card--back .card__logo { left: 56%; width: 40%; top: 32%; }
  .card--back .wordmark { font-size: 3.6em; }
  .card--back .slogan { color: var(--ink); font-size: 1em; margin-top: 0.3em; }
  .card--back.card--large .slogan { font-size: 1.05em; }

  .card__person { position: absolute; left: 9.8%; top: 19%; }
  .card__person .name { color: var(--gold); font-size: 1.6em; font-weight: 600; letter-spacing: 0.01em; line-height: 1.2; }
  .card__person .role { color: var(--ink); font-size: 1.05em; margin-top: 0.3em; }

  .card__contacts { position: absolute; left: 5%; top: 70%; list-style: none; }
  .card__contacts li { display: flex; align-items: center; gap: 1.6em; color: var(--gold); font-size: 1.02em; height: 1.65em; }
  .card__contacts svg { width: 1em; height: 1em; flex: none; fill: none; stroke: var(--ink); stroke-width: 1.6; }

  .card__divider { position: absolute; left: 49.5%; top: 74%; width: 0.9em; height: 4em; border-left: 1px solid var(--gold); border-right: 1px solid var(--gold); }
  .card__divider::after { content: ""; position: absolute; left: 50%; top: 0.6em; bottom: 0.6em; border-left: 1px solid var(--gold); }
  .card__address { position: absolute; left: 61.5%; top: 77%; color: var(--gold); font-size: 1.02em; line-height: 1.6; }
</style>
</head>
<body>
  <section class="board-left">
    <div class="hero-photo" role="img" aria-label="Photo of a russet dog carrying a stick through a woodland path"></div>
    <div class="brand-panel"><span class="wordmark">Brimovex</span></div>
    <div class="about-panel">
      <p>Lorem ipsum dolor sit amet, consectetur adipiscing elit, sed do eiusmod tempor incididunt ut labore et dolore magna aliqua. Quis ipsum suspendisse ultrices gravida. Risus commodo viverra maecenas accumsan lacus vel</p>
    </div>
  </section>

  <div class="stage-top"></div>
  <div class="stage-bottom"></div>

  <article class="card card--small card--front" style="left:457px; top:195px;">
    <div class="card__logo"><span class="wordmark">Brimovex</span><span class="slogan">Your furry friends deserves<br>the best</span></div>
    <div class="site">www.brimovex.com.au</div>
  </article>
  <article class="card card--small card--back" style="left:818px; top:195px;">
    <div class="card__person"><p class="name">DELIA RENSHAW</p><p class="role">Managing Director</p></div>
    <div class="card__logo"><span class="wordmark">Brimovex</span><span class="slogan">Your furry friends deserves<br>the best</span></div>
    <ul class="card__contacts">
      <li><svg viewBox="0 0 16 16"><path d="M4 2l2.5 3-1.5 1.5a8 8 0 0 0 4.5 4.5L11 9.5l3 2.5-1.5 2.2C7 14 2 9 1.8 3.5z"/></svg>+61 03 9000 4417</li>
      <li><svg viewBox="0 0 16 16"><rect x="1.5" y="3.5" width="13" height="9"/><path d="M1.5 3.5l6.5 5 6.5-5"/></svg>info@brimovex.com.au</li>
      <li><svg viewBox="0 0 16 16"><circle cx="8" cy="8" r="6.5"/><ellipse cx="8" cy="8" rx="2.8" ry="6.5"/><path d="M1.5 8h13"/></svg>www.brimovex.com.au</li>
    </ul>
    <div class="card__divider"></div>
    <p class="card__address">12/40 Larkin Road<br>Glen Ashby Vic 3160</p>
  </article>

  <article class="card card--large card--front" style="left:563px; top:564px;">
    <div class="card__logo"><span class="wordmark">Brimovex</span><span class="slogan">Your furry friends deserves<br>the best</span></div>
    <div class="site">www.brimovex.com.au</div>
  </article>
  <article class="card card--large card--back" style="left:563px; top:859px;">
    <div class="card__person"><p class="name">DELIA RENSHAW</p><p class="role">Managing Director</p></div>
    <div class="card__logo"><span class="wordmark">Brimovex</span><span class="slogan">Your furry friends deserves<br>the best</span></div>
    <ul class="card__contacts">
      <li><svg viewBox="0 0 16 16"><path d="M4 2l2.5 3-1.5 1.5a8 8 0 0 0 4.5 4.5L11 9.5l3 2.5-1.5 2.2C7 14 2 9 1.8 3.5z"/></svg>+61 03 9000 4417</li>
      <li><svg viewBox="0 0 16 16"><rect x="1.5" y="3.5" width="13" height="9"/><path d="M1.5 3.5l6.5 5 6.5-5"/></svg>info@brimovex.com.au</li>
      <li><svg viewBox="0 0 16 16"><circle cx="8" cy="8" r="6.5"/><ellipse cx="8" cy="8" rx="2.8" ry="6.5"/><path d="M1.5 8h13"/></svg>www.brimovex.com.au</li>
    </ul>
    <div class="card__divider"></div>
    <p class="card__address">12/40 Larkin Road<br>Glen Ashby Vic 3160</p>
  </article>
</body>
</html>
```